Coach/consultant in conflict and challenge needs an enticing flyer

I need a double sided DL flyer design that will describe my work in helping people meet conflict and emotional challenge so they can learn and grow from these difficulties. I want to give a flavour of my style through fresh colours, repeated images used differently (the spiral), and a sense of positivity around conflict and difficulty. I want to attract people who are keen to do things differently and want to engage with creative processes rather than getting stuck in familiar patterns. My work is creative and often includes use of story, images and fables, so I want to convey that as well. I also place the work in a spiritual context, but grounded in practicality so I don't want it to seem New Age or flakey. I want something that seems innovative, professional and intriguing. I've included a sample of something I mocked up in word and also a copy of a flyer for Marla Quennet's Ember Gathering that inspired me to get a DL flyer. I want the design to communicate trust and transformation and engaging with fresh ways of doing things by moving past old habits

Target Market(s)

Mid 30s plus women and men who want to change their approach to conflict and emotional difficulties and are willing to take the creative and challenging journey to do that

Industry/Entity Type

Learn

Colors
acd136
00a990

Requirements
Must have
• a shift in the use of the spiral image,
• use of image of me (Norah)
• bright fresh colours olours that represent growth and transformation--I've suggested lime green as it suggests a sense of growth
• easy to read text
Nice to have
• Interesting non-traditional fonts perhaps text in a contemporary sans serif and another brush script font (like the Ember Gathering example)
• bleed to the edge and run off the page images or text
Should not have
• anything that represents too much tradition or stuckness

```html
<!DOCTYPE html>
<html lang="en">
<head>
<meta charset="utf-8">
<title>Norah Ashdown – DL Flyer</title>
<link rel="stylesheet" href="https://fonts.googleapis.com/css2?family=Kalam:wght@700&family=Open+Sans:wght@400;600&display=swap">
<style>
  :root {
    --lime: #acd136;
    --lime-light: #cfe377;
    --lime-soft: #bfdc58;
    --brown: #7a4f32;
    --brown-light: #a57a52;
    --ink: #111;
    --white: #fff;
    --page: #e9ebe4;
  }
  * { box-sizing: border-box; margin: 0; padding: 0; }
  html, body { width: 1200px; height: 902px; overflow: hidden; background: var(--page); }
  body { position: relative; font-family: "Open Sans", Arial, sans-serif; color: var(--ink); }

  .card { position: absolute; width: 760px; background: var(--white); overflow: hidden;
          box-shadow: 0 6px 18px rgba(0,0,0,.18); }

  /* Front */
  .card--front { left: 40px; top: 40px; height: 380px; }
  .front__top { position: absolute; inset: 0 0 auto 0; height: 212px;
                background: linear-gradient(100deg, var(--lime) 0%, var(--lime-light) 45%, var(--lime-soft) 100%); }
  .front__band { position: absolute; left: 0; right: 0; top: 212px; height: 22px; background: var(--brown); }
  .spiral-art { position: absolute; border-radius: 50%;
                background: radial-gradient(circle, rgba(122,79,50,.35) 0%, rgba(165,122,82,.25) 55%, rgba(122,79,50,0) 72%); }
  .card--front .spiral-art { left: 70px; top: 30px; width: 160px; height: 160px; }
  .front__title { position: absolute; left: 300px; top: 20px; width: 420px; text-align: center;
                  font-family: "Kalam", cursive; color: var(--brown); }
  .front__name { font-size: 38px; line-height: 1.1; }
  .front__tags { font-size: 23px; line-height: 1.2; word-spacing: 4px; }
  .front__intro { position: absolute; left: 292px; top: 130px; width: 445px; font-size: 14px; line-height: 1.35; }
  .front__wordmark { position: absolute; left: 0; right: 0; top: 236px; height: 144px;
                     display: flex; align-items: center; justify-content: center;
                     font-family: "Kalam", cursive; font-size: 104px; color: var(--brown); }

  /* Back */
  .card--back { left: 400px; top: 470px; height: 392px; }
  .back__top { position: absolute; inset: 0 0 auto 0; height: 312px;
               background: linear-gradient(100deg, var(--lime) 0%, var(--lime-light) 50%, var(--lime-soft) 100%); }
  .back__backdrop { position: absolute; left: 170px; top: 20px; width: 300px; height: 300px; border-radius: 50%;
                    background: radial-gradient(circle, rgba(255,255,255,.18) 0%, rgba(255,255,255,0) 70%); }
  .back__copy { position: absolute; left: 36px; top: 52px; width: 460px; font-size: 14px; line-height: 1.38; text-align: justify; }
  .back__copy p + p { margin-top: 18px; }
  .services { position: absolute; left: 44px; top: 222px; width: 440px; list-style: none;
              display: grid; grid-template-columns: 215px 200px; row-gap: 10px; }
  .services li { display: flex; align-items: center; gap: 10px; font-size: 17px; font-weight: 600; letter-spacing: .3px; }
  .bullet { width: 16px; height: 16px; border-radius: 50%; border: 4px solid var(--brown); flex: none; }
  .portrait { position: absolute; left: 548px; top: 40px; width: 170px; height: 178px;
              background: linear-gradient(180deg, #8c8a84 0%, #c9b9a5 45%, #d6552b 75%, #c94420 100%); }
  .profile { position: absolute; left: 500px; top: 226px; width: 260px; text-align: center; font-family: "Kalam", cursive; color: var(--brown); }
  .profile__name { font-size: 27px; line-height: 1.1; }
  .profile__creds { font-size: 12px; }
  .contacts { position: absolute; left: 60px; top: 334px; display: grid; grid-template-columns: 210px 200px;
              row-gap: 10px; font-size: 11.5px; }
  .contacts span { display: flex; align-items: center; gap: 8px; }
  .contacts svg { width: 11px; height: 11px; fill: var(--lime); flex: none; }
  .abn { position: absolute; left: 515px; top: 334px; width: 190px; height: 28px; border-radius: 14px;
         background: var(--brown); color: var(--white); font-size: 15px; display: flex; align-items: center; justify-content: center; }
  .card--back .spiral-art { left: 668px; top: 300px; width: 100px; height: 100px; }
</style>
</head>
<body>

<section class="card card--front">
  <div class="front__top"></div>
  <div class="front__band"></div>
  <div class="spiral-art" role="img" aria-label="Brown brush-stroke spiral artwork"></div>
  <header class="front__title">
    <h1 class="front__name">Norah Ashdown</h1>
    <p class="front__tags"># courage &nbsp;# listening # creativity</p>
  </header>
  <p class="front__intro">Norah Ashdown is a coach, educator and mediator. She works with people who want to harvest the fruits of challenge and conflict so they live life differently.</p>
  <div class="front__wordmark">Norah ashdown</div>
</section>

<section class="card card--back">
  <div class="back__top"></div>
  <div class="back__backdrop" role="img" aria-label="Faint spiral backdrop"></div>
  <div class="back__copy">
    <p>Consult with Norah to address challenges in your life, relationship, group or organisation. Through listening, conversation and creative processes, you will discover what your challenge is asking of you. Norah Ashdown is a skilled facilitator who works to shift people’s responses from reactivity to creativity.</p>
    <p>With many years’ experience in coaching and mentorship, mediation and narrative processes, Norah supports you to uncover unique responses to difficult situations.</p>
  </div>
  <ul class="services">
    <li><span class="bullet"></span>CONSULTATIONS</li>
    <li><span class="bullet"></span>WORKSHOPS</li>
    <li><span class="bullet"></span>SPEAKING</li>
    <li><span class="bullet"></span>ARTICLES</li>
  </ul>
  <div class="portrait" role="img" aria-label="Portrait photograph of Norah Ashdown"></div>
  <div class="profile">
    <p class="profile__name">Norah Ashdown</p>
    <p class="profile__creds">PhD, MCR , BAppSci , DipHum, AssDipEd</p>
  </div>
  <div class="contacts">
    <span><svg viewBox="0 0 10 16"><rect x="1" y="0" width="8" height="16" rx="1.5"/></svg>0400 555 218</span>
    <span><svg viewBox="0 0 16 12"><path d="M0 0h16v12H0z M0 0l8 6 8-6" /></svg>norah@norahashdown.com</span>
    <span><svg viewBox="0 0 16 16"><path d="M3 1l3 3-2 2c1 2.5 3.5 5 6 6l2-2 3 3-2 2C7 15 1 9 1 3z"/></svg>+61 3 9000 4417</span>
    <span><svg viewBox="0 0 16 16"><circle cx="8" cy="8" r="8"/></svg>norahashdown.com</span>
  </div>
  <div class="abn">ABN 00 123 456 78</div>
  <div class="spiral-art" role="img" aria-label="Brown brush-stroke spiral artwork"></div>
</section>

</body>
</html>
```